Webdesign für  FAQ-Finder
Webdesign für FAQ-Finder
Zielgruppe
wiego-lumi.de ist ein FAQ-Finder für werdende / frisch gebackene Eltern in einem ansprechenden, effizienten und modernen Design.
Aufgabenstellung
Ein mobile first Designansatz basierenden auf einem cleanen, modernen Interface und Illustrationen im Stile von:
https://pixelkorb.example/shots/20581934-Tervon-a-fund-for-many
Es gibt noch kein Logo und kein CI. Die Farbwelt soll sich an dem Beispiel von
https://www.quarnetpantry.example/collections
orientieren. Gedeckt, warm. Thematisch geht es um Babies.
For structure perhaps like this:
https://pixelkorb.example/shots/20947715-Flexible-layout-for-Sitewerk-theming-service/attachments/7310452?mode=media
https://pixelkorb.example/shots/20633179--Staffing-Role-locator-Query-App
For Content:
https://www.wiegenpfad.example/category/themen/baby/

```html
<!DOCTYPE html>
<html lang="de">
<head>
<meta charset="utf-8">
<title>wiego-lumi.de – FAQ-Finder</title>
<link rel="stylesheet" href="https://fonts.googleapis.com/css2?family=Poppins:wght@500;600;700&family=Nunito:wght@400;600&display=swap">
<style>
  :root {
    --page-bg: #f2f2f2;
    --screen-bg: #ffffff;
    --ink: #1c1c2b;
    --primary: #2a5ea8;
    --primary-bright: #3e6ff2;
    --mint: #e3f0ec;
    --peach: #fbefe0;
    --sky-light: #dff3fb;
    --sky: #b9e3f4;
    --sofa: #5d9fe6;
    --sofa-dark: #2c4f7c;
    --grass: #3dbb83;
    --white: #ffffff;
    --indicator: #8a8a8a;
  }
  * { box-sizing: border-box; margin: 0; padding: 0; }
  html, body {
    width: 1200px; height: 960px; overflow: hidden;
    background: var(--page-bg);
  }
  .app-screen {
    position: absolute; left: 390px; top: 30px;
    width: 421px; height: 900px;
    background: var(--screen-bg);
    border-radius: 44px;
    overflow: hidden;
    box-shadow: 0 10px 40px rgba(0,0,0,0.08);
  }
  .status-bar {
    position: absolute; left: 0; top: 0; width: 100%; height: 50px;
  }
  .status-time {
    position: absolute; left: 40px; top: 19px;
    font: 600 12px/1 "Nunito", sans-serif; color: var(--ink);
  }
  .status-icons { position: absolute; right: 22px; top: 19px; }
  .deco-blob { position: absolute; }
  .deco-peach { left: 0; top: 92px; }
  .deco-mint { right: 0; top: 30px; }
  .menu-button {
    position: absolute; left: 26px; top: 79px; width: 26px; height: 18px;
  }
  .hero-title {
    position: absolute; left: 29px; top: 160px; width: 380px;
    font: 700 25px/33px "Poppins", sans-serif;
    color: var(--ink); letter-spacing: -0.2px;
  }
  .search-bar {
    position: absolute; left: 27px; top: 240px;
    width: 366px; height: 60px;
    border-radius: 30px; background: var(--primary);
    display: flex; align-items: center; justify-content: space-between;
    padding: 0 18px 0 19px;
  }
  .search-placeholder {
    font: 400 13.5px/1 "Nunito", sans-serif; color: var(--white);
  }
  .hero-illustration {
    position: absolute; left: 6px; top: 343px; width: 410px; height: 395px;
  }
  .cta-button {
    position: absolute; left: 106px; top: 770px; width: 208px; height: 53px;
    border-radius: 27px;
    background: linear-gradient(90deg, var(--primary), var(--primary-bright));
    display: flex; align-items: center; justify-content: center;
    font: 500 15.5px/1 "Poppins", sans-serif; color: var(--white);
    letter-spacing: 0.2px;
    text-decoration: none;
  }
  .home-indicator {
    position: absolute; left: 159px; top: 886px; width: 118px; height: 4px;
    border-radius: 2px; background: var(--indicator);
  }
</style>
</head>
<body>
  <main class="app-screen">
    <svg class="deco-blob deco-peach" width="90" height="160" viewBox="0 0 90 160" aria-hidden="true">
      <path d="M0 0 C40 10 85 40 84 75 C83 110 40 120 20 160 L0 160 Z" fill="var(--peach)"/>
    </svg>
    <svg class="deco-blob deco-mint" width="215" height="210" viewBox="0 0 215 210" aria-hidden="true">
      <path d="M60 0 L215 0 L215 190 C200 210 190 170 180 150 C165 120 130 150 110 120 C95 100 120 80 100 65 C80 50 50 90 25 80 C0 70 30 30 60 0 Z" fill="var(--mint)"/>
    </svg>

    <div class="status-bar">
      <span class="status-time">9:41</span>
      <svg class="status-icons" width="66" height="12" viewBox="0 0 66 12" aria-hidden="true">
        <rect x="0" y="8" width="3" height="4" rx="1" fill="var(--ink)"/>
        <rect x="4.5" y="6" width="3" height="6" rx="1" fill="var(--ink)"/>
        <rect x="9" y="3.5" width="3" height="8.5" rx="1" fill="var(--ink)"/>
        <rect x="13.5" y="1" width="3" height="11" rx="1" fill="#c8c8c8"/>
        <path d="M24 5 Q31 -1 38 5" stroke="var(--ink)" stroke-width="1.8" fill="none"/>
        <path d="M26.5 7.5 Q31 3.5 35.5 7.5" stroke="var(--ink)" stroke-width="1.8" fill="none"/>
        <circle cx="31" cy="10" r="1.5" fill="var(--ink)"/>
        <rect x="44" y="2" width="18" height="9" rx="2.5" fill="var(--ink)"/>
        <rect x="63" y="5" width="2" height="3" rx="1" fill="var(--ink)"/>
      </svg>
    </div>

    <svg class="menu-button" viewBox="0 0 26 18" aria-label="Menü" role="img">
      <rect y="0" width="26" height="3" rx="1.5" fill="var(--ink)"/>
      <rect y="7.5" width="26" height="3" rx="1.5" fill="var(--ink)"/>
      <rect y="15" width="26" height="3" rx="1.5" fill="var(--ink)"/>
    </svg>

    <h1 class="hero-title">Hier finden Sie alle<br>Themen rund um das Baby</h1>

    <div class="search-bar" role="search">
      <span class="search-placeholder">Geburtsvorbereitung , Schwangerschaft , Stillen</span>
      <svg width="26" height="26" viewBox="0 0 26 26" aria-hidden="true">
        <circle cx="11" cy="11" r="9" stroke="var(--white)" stroke-width="1.6" fill="none"/>
        <line x1="17.5" y1="17.5" x2="24" y2="24" stroke="var(--white)" stroke-width="1.8" stroke-linecap="round"/>
      </svg>
    </div>

    <svg class="hero-illustration" viewBox="0 0 410 395" role="img" aria-label="Illustration: Frau sitzt mit Laptop auf einem blauen Sofa, daneben Stehlampe und Zimmerpflanze, auf grünem Teppich">
      <defs>
        <linearGradient id="sceneTone" x1="0.2" y1="0" x2="0.5" y2="1">
          <stop offset="0" stop-color="var(--sky-light)"/>
          <stop offset="0.35" stop-color="var(--sky)"/>
          <stop offset="0.62" stop-color="var(--sofa)"/>
          <stop offset="0.8" stop-color="var(--sofa-dark)"/>
          <stop offset="1" stop-color="var(--grass)"/>
        </linearGradient>
      </defs>
      <path d="M40 60 C60 0 150 -5 200 30 C250 50 320 10 370 40 C415 70 405 150 385 200 C370 240 405 290 380 330 C350 390 300 360 250 370 C200 385 120 360 70 340 C20 320 0 270 10 220 C20 170 20 110 40 60 Z" fill="url(#sceneTone)"/>
    </svg>

    <a class="cta-button" href="#themen">HÄUFIGSTE THEMEN</a>

    <div class="home-indicator"></div>
  </main>
</body>
</html>
```